Broschüre für Immobilienvertrieb
Zielgruppe
Wir sind ein Immobilienvertrieb im Bereich Neubau-Immobilien und Bestand-Immobilien aus München. Die Firma BLOR existiert seit über 30 Jahren. Vor 4 Jahren haben wir ein cooles modernes Rebranding durchgeführt, sodass man mit unserem neuen Corporate Design richtig Spaß am Gestalten haben kann.
Eine konkrete Zielgruppe zu definieren ist schwierig, da unsere Käufer von 20-80 Jahren sein können. Ob junge, erfolgreiche Menschen, junge Familien, ältere Erwachsene, die von sich nach Auszug ihrer Kinder von ihrem Haus trennen wollen und eine kleinere Wohnung suchen oder einfach der Kapitalanleger, der auf der Suche nach einer neuen Investition ist.
Unsere CI ist gradlinig und setzt sich aus anthrazit, neonorange und weiß zusammen (Styleguide ist anbei).
Im Bestand gibt es nicht pro Objekt ein CI, hier wird mit dem der BLOR gearbeitet. Im Neubau hat jedes einzelne Projekt sein eigenes CI (siehe aktuell zeltholm.de).
www.blor.de
Aufgabenstellung
Zur Aufgabe: Für die Bestandimmobilien benötigen wir ein neues Layout eines Immobilienexposé. Das Exposé wird sowohl online verwendet als auch von uns selbst gedruckt und gebunden.
Input: beigefügt ein Beispielexposé - grundsätzlich gefällt uns das Design, wir möchten jedoch etwas NEUES, modernes. Bitte keine Kopien des alten Exposés, dies soll nur als Input dienen (gerne können die Daten der Wohnung für den neuen Designentwurf genutzt werden).
Die Datei soll von uns befüllbar sein, sodass wir Texte und Bilder selbst austauschen können.
Für die Onlinenutzung gerne als doppelseitige Datei, zum Beispiel um Bilder über zwei Seiten größer und schöner darstellen zu können (Auszug Beispielimmobilie anbei). Für den Druck wird die Datei zudem mit Einzelseiten benötigt.

```html
<!DOCTYPE html>
<html lang="de">
<head>
<meta charset="utf-8">
<title>BLOR Exposé – Lindenallee München</title>
<link href="https://fonts.googleapis.com/css2?family=Montserrat:wght@400;500;600;700&display=swap" rel="stylesheet">
<style>
  :root {
    --anthracite: #25282c;
    --anthracite-soft: #2d3035;
    --neon-orange: #e8482c;
    --orange-light: #f28a55;
    --white: #ffffff;
    --paper-bg: #e7e4df;
    --text-dark: #23262a;
  }
  * { margin: 0; padding: 0; box-sizing: border-box; }
  html, body { width: 1200px; height: 900px; overflow: hidden; }
  body {
    background: var(--paper-bg);
    font-family: "Montserrat", sans-serif;
    color: var(--white);
    position: relative;
  }
  .abs { position: absolute; }

  /* ---------- Cover ---------- */
  .cover {
    left: 38px; top: 228px; width: 370px; height: 517px;
    background: var(--anthracite-soft);
    overflow: hidden;
  }
  .cover-visual {
    left: 0; top: 0; width: 370px; height: 370px;
    background: linear-gradient(160deg, #e9633c 0%, #f08a52 45%, #e4693f 100%);
  }
  .cover-frame { background: var(--white); }
  .cover-brand {
    left: 0; width: 370px; top: 68px; text-align: center;
    font-weight: 600; font-size: 26px; letter-spacing: 6px;
  }
  .cover-tagline {
    left: 0; width: 370px; top: 123px; text-align: center;
    font-weight: 700; font-size: 8.5px; letter-spacing: 1.6px;
  }
  .cover-title {
    left: 0; width: 370px; top: 405px; text-align: center;
    font-weight: 600; font-size: 15px; letter-spacing: 2.6px; line-height: 18px;
  }
  .cover-subtitle {
    left: 0; width: 370px; top: 447px; text-align: center;
    font-weight: 400; font-size: 8.4px; letter-spacing: 1.3px; line-height: 10.5px;
  }
  .cover-object {
    left: 18px; top: 493px;
    font-weight: 600; font-size: 7px; letter-spacing: 0.9px;
  }

  /* ---------- Spread: left page ---------- */
  .page-left {
    left: 439px; top: 231px; width: 360px; height: 515px;
    background: var(--anthracite);
    overflow: hidden;
  }
  .page-number { font-size: 5.5px; font-weight: 600; }
  .section-title {
    left: 20px; top: 58px; font-size: 15px; letter-spacing: 1.6px; font-weight: 400;
  }
  .section-title .plus { color: var(--neon-orange); font-weight: 700; margin-right: 3px; }
  .section-title strong { color: var(--neon-orange); font-weight: 700; }
  .object-address {
    left: 20px; top: 97px; font-size: 8.4px; font-weight: 700; letter-spacing: 1.3px; line-height: 10.5px;
  }
  .body-text {
    font-size: 6.9px; line-height: 11px; text-align: justify; font-weight: 400;
  }
  .body-text p + p { margin-top: 11px; }
  .body-text b { font-weight: 700; }
  .col-1 { left: 20px; top: 150px; width: 152px; }
  .col-2 { left: 190px; top: 149px; width: 152px; }
  .district-dot {
    left: -24px; top: 306px; width: 92px; height: 92px; border-radius: 50%;
    background: var(--neon-orange);
  }
  .district-name {
    left: 0; top: 318px;
    font-weight: 700; font-size: 44px; letter-spacing: 3px; line-height: 38px;
  }
  .district-name span { display: block; white-space: nowrap; }
  .district-name .line-1 { margin-left: -12px; }
  .district-name .line-2 { margin-left: 13px; }
  .district-name .line-3 { margin-left: -1px; }
  .footer-rule { background: var(--white); }
  .footer-note { font-size: 5.4px; font-weight: 400; text-align: center; }
  .footer-note b { font-weight: 700; }

  /* ---------- Spread: right page ---------- */
  .page-right {
    left: 799px; top: 231px; width: 359px; height: 515px;
    background: var(--white);
    overflow: hidden;
    color: var(--text-dark);
  }
  .accent-line { background: var(--neon-orange); }
  .building-visual {
    left: 0; top: 32px; width: 338px; height: 234px;
    background: linear-gradient(135deg, #8c97a6 0%, #c9cfd6 40%, #b9806a 75%, #6f4a3f 100%);
  }
  .orange-panel {
    left: 239px; top: 151px; width: 99px; height: 172px;
    background: linear-gradient(180deg, rgba(240,120,70,0.92), #ef8a57);
  }
  .contact {
    right: 21px; top: 340px; text-align: right;
    font-size: 7.4px; font-weight: 700; letter-spacing: 0.3px; line-height: 11px;
  }
  .contact .label { color: var(--neon-orange); }
  .contact p + p { margin-top: 11px; }
  .seal {
    left: 297px; top: 439px; width: 40px; height: 40px; border-radius: 50%;
    border: 1.5px solid var(--neon-orange);
  }
</style>
</head>
<body>

  <!-- Cover -->
  <section class="cover abs" aria-label="Titelseite">
    <div class="cover-visual abs" role="img" aria-label="Hochhausfassade mit Balkonen, orange eingefärbt"></div>
    <div class="cover-frame abs" style="left:19px;top:17px;width:2px;height:469px"></div>
    <div class="cover-frame abs" style="left:19px;top:17px;width:245px;height:2px"></div>
    <div class="cover-frame abs" style="left:350px;top:17px;width:2px;height:483px"></div>
    <div class="cover-frame abs" style="left:107px;top:498px;width:245px;height:2px"></div>
    <div class="cover-brand abs">BLOR</div>
    <div class="cover-tagline abs">RÄUME MIT HALTUNG</div>
    <h1 class="cover-title abs">LINDENALLEE<br>MÜNCHEN</h1>
    <p class="cover-subtitle abs">MÖBILIERTE &amp; GUT VERMIETETE KAPITALANLAGE<br>IN GUTER LAGE MIT BALKON &amp; STELLPLATZ</p>
    <p class="cover-object abs">OBJEKT XX - 2.OG</p>
  </section>

  <!-- Spread left page -->
  <section class="page-left abs" aria-label="Seite 2">
    <div class="abs" style="left:0;top:18px;width:12px;height:3px;background:var(--white)"></div>
    <div class="page-number abs" style="left:21px;top:17px">2</div>
    <h2 class="section-title abs"><span class="plus">+</span>OBJEKT<strong>ADRESSE</strong></h2>
    <p class="object-address abs">OBJEKT 178<br>LINDENALLEE 206<br>WHG. 2202<br>80804 MÜNCHEN</p>

    <div class="body-text col-1 abs">
      <p>Im Stadtteil Schwabing gelegen, gehört dieses im Jahr <b>1972</b> erbaute Gebäude zur Münchner Geschichte. Ehemals als Hotel für den Sternbau geplant, kennt jeder richtige Münchner mindestens eine Person, die hier einmal gewohnt hat. Durch diverse Modernisierungen und Sanierungen in den Jahren von <b>2012</b> bis <b>heute</b> ist das Objekt in einem guten, modernen Zustand. Überwiegend <b>1-Zimmer-Apartments</b> verteilen sich hier auf 15 Etagen.</p>
    </div>

    <div class="body-text col-2 abs">
      <p>Die helle, <b>vollmöblierte Wohnung</b> besticht durch einen praktisch geschnittenen Grundriss und ist mit einem Laminatboden ausgestattet. Im Flur befindet sich ein geräumiger Einbauschrank der perfekten Stauraum bietet. Der Wohn-/Schlafraum ist mit einem Bett, Esstisch mit Stühlen sowie einer modernen Schrankwand mit TV ausgestattet.</p>
      <p>Die Ausstattung der kleinen, separaten Küche mit Fliesenboden besteht aus einer Einbauküche mit Kühlschrank und Mikrowelle. Die Wohnung verfügt über ein weiß gefliestes Bad mit Wanne, WC, Waschbecken mit Unterschrank und Decken-Downlights. Der <b>große Balkon</b>, von welchem Sie bis in die späten Abendstunden die Sonne genießen können, lädt zum Verweilen ein. Ebenfalls gehören ein Kellerabteil sowie ein Außenstellplatz zur Wohnung.</p>
      <p>Die Wohnung ist seit dem <b>01.10.2022</b> mit einer Kaltmiete von <b>975 €/Monat</b> zzgl. einer jährlichen Staffel von 30€ vermietet. Diese Staffel besteht für weitere vier Jahre. Der zugehörige Außenstellplatz ist für 70 €/Monat vermietet.</p>
    </div>

    <div class="district-dot abs"></div>
    <div class="district-name abs"><span class="line-1">SCH</span><span class="line-2">WAB</span><span class="line-3">ING</span></div>

    <div class="footer-rule abs" style="left:0;top:478px;width:360px;height:2px"></div>
    <p class="footer-note abs" style="left:0;top:493px;width:360px"><b>Exposé</b> | Lindenallee 206 | Objektnr. XX - München</p>
  </section>

  <!-- Spread right page -->
  <section class="page-right abs" aria-label="Seite 3">
    <div class="page-number abs" style="left:334px;top:15px">3</div>
    <div class="accent-line abs" style="left:343px;top:15px;width:12px;height:4px"></div>
    <div class="accent-line abs" style="left:16px;top:0;width:2px;height:480px"></div>
    <div class="accent-line abs" style="left:0;top:478px;width:18px;height:2px"></div>
    <div class="building-visual abs" role="img" aria-label="Hochhaus mit roten Balkonen vor Wolkenhimmel"></div>
    <div class="orange-panel abs"></div>

    <div class="contact abs">
      <p>BLOR IMMOBILIEN GMBH<br>LINDENALLEE 204A<br>80804 MÜNCHEN</p>
      <p><span class="label">T.</span> 089.40 512-700<br><span class="label">M.</span> INFO@BLOR.DE</p>
      <p><span class="label">W.</span> BLOR.DE</p>
    </div>
    <div class="seal abs"></div>

    <p class="footer-note abs" style="left:0;top:493px;width:359px;color:var(--text-dark)"><b>Exposé</b> | Lindenallee 206 | Objektnr. XX - München</p>
  </section>

</body>
</html>
```